" somos uma clinica onde temos profissionais atendendo em diversas especialidades da medicina e da odontologia, oferecendo serviços como exames radiologicos, consultas, cirurgias, etc. "

```html
<!DOCTYPE html>
<html lang="pt-BR">
<head>
<meta charset="utf-8">
<title>Clínica Sereno – Envelopes</title>
<link rel="stylesheet" href="https://fonts.googleapis.com/css2?family=Montserrat:wght@400;500&display=swap">
<style>
  :root {
    --backdrop: #e9ebee;
    --paper: #ffffff;
    --paper-edge: #dcdfe3;
    --brand-navy: #1f4f7c;
    --flap-top: #1b5a8c;
    --flap-bottom: #0f3f68;
    --text-grey: #4a5560;
    --mark-faint: #e4ecf2;
  }
  html, body {
    margin: 0;
    width: 1200px;
    height: 1200px;
    overflow: hidden;
    background: var(--backdrop);
    font-family: "Montserrat", sans-serif;
  }
  .stationery {
    position: relative;
    width: 1200px;
    height: 1200px;
  }
  .envelope {
    position: absolute;
    left: 120px;
    width: 960px;
    height: 480px;
    background: var(--paper);
    box-shadow: 0 2px 0 var(--paper-edge), 0 14px 30px rgba(0,0,0,0.12);
    overflow: hidden;
  }
  .envelope--front { top: 80px; }
  .envelope--back { top: 640px; }

  .faint-mark {
    position: absolute;
    left: -60px;
    top: 20px;
    width: 300px;
    height: 300px;
    border-radius: 50%;
    background: var(--mark-faint);
  }
  .brand {
    position: absolute;
    display: flex;
    align-items: center;
    gap: 14px;
    color: var(--brand-navy);
    font-weight: 400;
    letter-spacing: 0.08em;
    text-transform: uppercase;
    white-space: nowrap;
  }
  .brand__dot {
    border-radius: 50%;
    background: var(--brand-navy);
  }
  .envelope--front .brand {
    left: 430px;
    top: 150px;
    font-size: 46px;
  }
  .envelope--front .brand__dot { width: 22px; height: 22px; }
  .envelope--back .brand {
    right: 50px;
    bottom: 58px;
    font-size: 18px;
    gap: 8px;
  }
  .envelope--back .brand__dot { width: 10px; height: 10px; }

  .flap {
    position: absolute;
    left: 0;
    top: 0;
    width: 960px;
    height: 110px;
  }
  .contact {
    position: absolute;
    left: 330px;
    bottom: 52px;
    display: grid;
    grid-template-columns: 150px 170px;
    column-gap: 16px;
    row-gap: 10px;
    margin: 0;
    padding: 0;
    list-style: none;
    font-size: 10px;
    line-height: 1.35;
    color: var(--text-grey);
  }
  .contact__item {
    display: flex;
    align-items: flex-start;
    gap: 7px;
    white-space: nowrap;
  }
  .contact__icon {
    flex: none;
    width: 14px;
    height: 14px;
  }
</style>
</head>
<body>
<main class="stationery">

  <section class="envelope envelope--front" aria-label="Envelope, frente">
    <div class="faint-mark"></div>
    <div class="brand">
      <span class="brand__dot"></span>
      <span class="brand__name">Clínica Sereno</span>
    </div>
  </section>

  <section class="envelope envelope--back" aria-label="Envelope, verso">
    <svg class="flap" viewBox="0 0 960 110" aria-hidden="true">
      <defs>
        <linearGradient id="flapGradient" x1="0" y1="0" x2="0" y2="1">
          <stop offset="0" stop-color="var(--flap-top)"/>
          <stop offset="1" stop-color="var(--flap-bottom)"/>
        </linearGradient>
      </defs>
      <path d="M0 0 H960 V70 Q960 110 920 110 H40 Q0 110 0 70 Z" fill="url(#flapGradient)"/>
    </svg>

    <ul class="contact">
      <li class="contact__item">
        <svg class="contact__icon" viewBox="0 0 14 14"><circle cx="7" cy="7" r="7" fill="var(--text-grey)"/><path d="M4.6 3.6l1.2 1.2-.6 1c.5 1 1.2 1.7 2.2 2.2l1-.6 1.2 1.2-.8 1.2C6.6 9.6 4.4 7.4 3.6 4.4z" fill="#fff"/></svg>
        <span>(11) 3456-7890</span>
      </li>
      <li class="contact__item">
        <svg class="contact__icon" viewBox="0 0 14 14"><circle cx="7" cy="7" r="7" fill="var(--text-grey)"/><path d="M4.6 3.6l1.2 1.2-.6 1c.5 1 1.2 1.7 2.2 2.2l1-.6 1.2 1.2-.8 1.2C6.6 9.6 4.4 7.4 3.6 4.4z" fill="#fff"/></svg>
        <span>(11) 98765-4321</span>
      </li>
      <li class="contact__item">
        <svg class="contact__icon" viewBox="0 0 14 14"><circle cx="7" cy="7" r="7" fill="var(--text-grey)"/><path d="M7 3a2.4 2.4 0 0 1 2.4 2.4C9.4 7.2 7 10.6 7 10.6S4.6 7.2 4.6 5.4A2.4 2.4 0 0 1 7 3z" fill="#fff"/><circle cx="7" cy="5.4" r=".9" fill="var(--text-grey)"/></svg>
        <span>Rua das Flores, 120<br>Centro, São Paulo</span>
      </li>
      <li class="contact__item">
        <svg class="contact__icon" viewBox="0 0 14 14"><circle cx="7" cy="7" r="7" fill="var(--text-grey)"/><rect x="3.5" y="4.5" width="7" height="5" fill="#fff"/><path d="M3.5 4.5L7 7.3l3.5-2.8" fill="none" stroke="var(--text-grey)" stroke-width=".7"/></svg>
        <span>contato@sereno.med.br</span>
      </li>
    </ul>

    <div class="brand">
      <span class="brand__dot"></span>
      <span class="brand__name">Clínica Sereno</span>
    </div>
  </section>

</main>
</body>
</html>
```